Business Card Design Project

New Business Card design for Varodine Technology Ltd using new Logo and new Tagline for staffing company.

About us from our website - www.varodine.example:

VaroDine is a leading and recognized Electronic Entertainment, Workforce Augmentation, and Project Management solutions provider with clients in Electronic Entertainment, Legal, Technology, Government and other verticals that range in size from start up organizations to Zenlar 500 companies. VaroDine is certified as an 8(a) minority and woman owned enterprise, established in 1998.

Target Market(s)

Companies in Electronic Entertainment, Legal, Government and Technology

Industry/Entity Type

Business

Requirements
Must have
• Must include in small letters the following information on back:

Established in 1998
8(a)(w)(e), Cage #7KRT9, DUNS #462137580

Front should have the following:
Derek Holloway
Vice President
5820 Birchmont Road
Fallowby, FB 482917
555-318-2746 X 100
555-902-6613 Fax
555-318-2746 Toll Free
name@varodine.example

Our Tagline: Connect • Collaborate • Achieve

```html
<!DOCTYPE html>
<html lang="en">
<head>
<meta charset="utf-8">
<title>VaroDine Business Card</title>
<link rel="stylesheet" href="https://fonts.googleapis.com/css2?family=Source+Sans+3:wght@400;600;700&display=swap">
<style>
  :root {
    --logo-blue: #0a2cf2;
    --logo-blue-66: #6a7ef5;
    --logo-black: #0b0b0b;
    --black-66: #4a4b4d;
    --paper: #ffffff;
    --text-dark: #111111;
    --text-light: #e6e6e6;
    --rule-grey: #8e8e8e;
  }
  * { box-sizing: border-box; margin: 0; padding: 0; }
  html, body { width: 1200px; height: 566px; overflow: hidden; background: var(--paper); }
  body { font-family: "Source Sans 3", "Myriad Pro", Arial, sans-serif; color: var(--text-dark); }
  .board { position: relative; width: 1200px; height: 566px; overflow: hidden; }

  /* Front card */
  .card-front {
    position: absolute; left: 45px; top: 12px; width: 507px; height: 321px;
    background: var(--logo-blue-66);
    border-radius: 0 0 24px 10px; overflow: hidden;
  }
  .card-front .circuit-field {
    position: absolute; inset: 0;
    background: linear-gradient(120deg, rgba(255,255,255,0.10), rgba(255,255,255,0) 55%, rgba(255,255,255,0.08));
  }
  .card-front .accent-rule { position: absolute; left: 0; top: 0; }
  .contact { position: absolute; left: 63px; top: 28px; line-height: 22px; font-size: 16px; }
  .contact .name, .contact .title { font-weight: 700; font-size: 18px; line-height: 23px; }
  .contact .address { margin-top: 25px; }
  .tagline { position: absolute; left: 63px; top: 288px; font-size: 16px; }
  .logo-plate {
    position: absolute; left: 335px; top: 105px; width: 172px; height: 111px;
    background: var(--logo-black);
    display: flex; align-items: center; justify-content: center; gap: 8px;
  }
  .wordmark { font-weight: 700; color: var(--paper); letter-spacing: -0.5px; }
  .logo-plate .wordmark { font-size: 27px; }
  .mark-dot { border-radius: 50%; background: var(--logo-blue); flex: none; }
  .logo-plate .mark-dot { width: 14px; height: 14px; }

  /* Back card */
  .card-back {
    position: absolute; left: 616px; top: 18px; width: 506px; height: 318px;
    background: var(--logo-black);
    border-radius: 0 28px 0 28px; overflow: hidden;
  }
  .card-back .brand {
    position: absolute; left: 0; right: 0; top: 115px;
    display: flex; align-items: center; justify-content: center; gap: 16px;
  }
  .card-back .wordmark { font-size: 58px; }
  .card-back .mark-dot { width: 26px; height: 26px; }
  .credentials {
    position: absolute; right: 12px; top: 228px; text-align: right;
    color: var(--text-light); font-size: 15px; line-height: 22px;
  }
  .card-back .base-rule { position: absolute; left: 125px; top: 276px; }

  /* Board labels */
  .side-label { position: absolute; top: 350px; font-weight: 700; font-size: 18px; }
  .side-label.front { left: 250px; }
  .side-label.back { left: 833px; }

  /* Colour key */
  .palette { position: absolute; top: 522px; left: 0; width: 100%; height: 44px; }
  .swatch { position: absolute; top: 0; width: 42px; height: 44px; }
  .swatch-name { position: absolute; top: 20px; font-weight: 700; font-size: 18px; }
</style>
</head>
<body>
<main class="board">

  <section class="card-front" aria-label="Business card front">
    <div class="circuit-field" role="img" aria-label="Light circuit-trace line pattern across the blue background"></div>
    <svg class="accent-rule" width="40" height="240" aria-hidden="true">
      <line x1="22" y1="0" x2="22" y2="218" stroke="#c9d0fb" stroke-width="3"/>
      <circle cx="22" cy="220" r="5" fill="#c9d0fb"/>
    </svg>
    <div class="contact">
      <p class="name">Derek Holloway</p>
      <p class="title">Vice President</p>
      <p class="address">5820 Birchmont Road</p>
      <p>Fallowby, FB 482917</p>
      <p>555-318-2746 X 100</p>
      <p>555-902-6613 Fax</p>
      <p>555-318-2746 Toll Free</p>
      <p>name@varodine.example</p>
    </div>
    <p class="tagline">Our Tagline: Connect • Collaborate • Achieve</p>
    <div class="logo-plate">
      <span class="wordmark">VaroDine</span>
      <span class="mark-dot"></span>
    </div>
  </section>

  <section class="card-back" aria-label="Business card back">
    <div class="brand">
      <span class="wordmark">VaroDine</span>
      <span class="mark-dot"></span>
    </div>
    <div class="credentials">
      <p>Established in 1998</p>
      <p>8(a)(w)(e), Cage #7KRT9, DUNS #462137580</p>
    </div>
    <svg class="base-rule" width="385" height="12" aria-hidden="true">
      <circle cx="5" cy="6" r="4" fill="var(--rule-grey)"/>
      <line x1="5" y1="6" x2="385" y2="6" stroke="var(--rule-grey)" stroke-width="2"/>
    </svg>
  </section>

  <p class="side-label front">Front</p>
  <p class="side-label back">Back</p>

  <div class="palette" aria-label="Colour key">
    <span class="swatch" style="left:135px; background:var(--logo-blue)"></span>
    <span class="swatch-name" style="left:183px">Logo Blue</span>
    <span class="swatch" style="left:297px; background:var(--logo-blue-66)"></span>
    <span class="swatch-name" style="left:355px">66% Logo Blue</span>
    <span class="swatch" style="left:507px; background:var(--logo-black)"></span>
    <span class="swatch-name" style="left:557px">Logo Black</span>
    <span class="swatch" style="left:674px; background:var(--black-66)"></span>
    <span class="swatch-name" style="left:730px">66%&nbsp; Black</span>
  </div>

</main>
</body>
</html>
```